Business Card Design Quokka Celebration Co

on the front i would like to see the logo and my contact details. on the back i would like it to include the 3 parts to the business party planning, party hire and party supplies also with a line at the bottom (or white space) to write their appointment details.

Target Market(s)

mums and corporates

Industry/Entity Type

Business

Requirements
Must have
• logo and contact details which are: Name: Janelle, Phone: 0417263954, email: jan@quokkaevents.com.au, Website: www.quokkaevents.com.au,

```html
<!DOCTYPE html>
<html lang="en">
<head>
<meta charset="utf-8">
<title>Quokka Celebration Co — Business Card</title>
<link href="https://fonts.googleapis.com/css2?family=Arimo:wght@400;700&family=Oregano:ital@1&display=swap" rel="stylesheet">
<style>
  :root {
    --purple: #5a3a9c;
    --magenta: #c93a9e;
    --yellow: #f7b51c;
    --cyan: #11b4d6;
    --ink-border: #000000;
    --paper: #ffffff;
  }
  html, body {
    margin: 0;
    padding: 0;
    width: 1200px;
    height: 889px;
    overflow: hidden;
    background: var(--paper);
  }
  .canvas {
    position: relative;
    width: 1200px;
    height: 889px;
    font-family: "Arimo", Arial, sans-serif;
  }

  /* Front */
  .card-front {
    position: absolute;
    left: 21px; top: 21px;
    width: 550px; height: 847px;
    box-sizing: border-box;
    border: 2px solid var(--ink-border);
    background: var(--paper);
  }
  .front-wordmark {
    position: absolute;
    left: 0; right: 0; top: 120px;
    height: 440px;
    display: flex;
    align-items: center;
    justify-content: center;
    text-align: center;
    font-weight: 700;
    font-size: 54px;
    line-height: 1.1;
    color: var(--purple);
  }
  .front-contact {
    position: absolute;
    right: 26px; top: 680px;
    text-align: right;
    color: var(--purple);
  }
  .contact-name { font-size: 40px; line-height: 1.1; margin: 0 0 4px; }
  .contact-line { font-size: 24px; line-height: 35px; margin: 0; }

  /* Back */
  .card-back {
    position: absolute;
    left: 630px; top: 21px;
    width: 552px; height: 851px;
    overflow: hidden;
  }
  .balloon-field {
    position: absolute;
    inset: 0;
    background: linear-gradient(160deg, var(--purple) 0%, var(--magenta) 40%, var(--yellow) 70%, var(--cyan) 100%);
  }
  .back-logo-panel {
    position: absolute;
    left: 109px; top: 0;
    width: 334px; height: 295px;
    background: var(--paper);
    display: flex;
    align-items: center;
    justify-content: center;
  }
  .back-wordmark {
    text-align: center;
    font-weight: 700;
    font-size: 30px;
    line-height: 1.15;
    color: var(--purple);
  }
  .back-info-panel {
    position: absolute;
    left: 109px; top: 346px;
    width: 334px; height: 505px;
    background: var(--paper);
  }
  .services {
    list-style: none;
    margin: 0; padding: 0;
    position: absolute;
    left: 0; right: 0; top: 28px;
    text-align: center;
    font-family: "Oregano", cursive;
    font-style: italic;
    font-size: 40px;
    line-height: 53px;
    color: var(--purple);
  }
  .appointment-label {
    position: absolute;
    left: 0; right: 0; top: 232px;
    text-align: center;
    font-size: 20px;
    color: var(--purple);
    margin: 0;
  }
  .appointment-grid {
    position: absolute;
    left: 0; top: 0;
    width: 334px; height: 505px;
  }
  .col-label {
    position: absolute;
    top: 272px;
    font-size: 19px;
    color: var(--purple);
  }
  .col-date { left: 15px; }
  .col-time { left: 226px; }
</style>
</head>
<body>
<main class="canvas">

  <section class="card-front">
    <div class="front-wordmark">Quokka<br>Celebration Co</div>
    <div class="front-contact">
      <p class="contact-name">Janelle</p>
      <p class="contact-line">0417263954</p>
      <p class="contact-line">jan@quokkaevents.com.au</p>
      <p class="contact-line">www.quokkaevents.com.au</p>
    </div>
  </section>

  <section class="card-back">
    <div class="balloon-field" role="img" aria-label="Decorative background of large party balloons in purple, magenta, yellow and cyan"></div>

    <div class="back-logo-panel">
      <div class="back-wordmark">Quokka<br>Celebration Co</div>
    </div>

    <div class="back-info-panel">
      <ul class="services">
        <li>Party Planning</li>
        <li>Party Hire</li>
        <li>Party Supplies</li>
      </ul>
      <p class="appointment-label">APPOINTMENT:</p>
      <span class="col-label col-date">DATE</span>
      <span class="col-label col-time">TIME</span>
      <svg class="appointment-grid" viewBox="0 0 334 505" aria-hidden="true">
        <g stroke="#5a3a9c" stroke-width="2">
          <line x1="216" y1="263" x2="216" y2="505"/>
          <line x1="15" y1="330" x2="320" y2="330"/>
          <line x1="15" y1="381" x2="320" y2="381"/>
          <line x1="15" y1="432" x2="320" y2="432"/>
          <line x1="15" y1="484" x2="320" y2="484"/>
        </g>
      </svg>
    </div>
  </section>

</main>
</body>
</html>
```